Business Card with PUNCH
bluepinelodge.net
Project: Business Card with PUNCH
Business Card with PUNCH - Consulting
Creative Brief
Simple
Morris Trulsow
President
418 Dunmere Lane Suite 207 Spring, TX 77291
morris@bluepinelodge.net
logo on the back please
mtrulsow mtrulsow
WOW, what a tremendous effort overnight! Here is what I can tell you from what we have seen so far: 1. Prefer horizontal orientation of card rather than vertical. 2. Prefer the white cards with the blue and gray logo vs. the darker colors 3. Would like the back of the card to be white with room for a hand written note 4. Clear plastic cards are not a hit 5. Not a fan of card that look like the data is presented on any kind of a 'tab' or website type icons. Thanks for the many creative ideas, we are excited about this contest. mt

```html
<!DOCTYPE html>
<html lang="en">
<head>
<meta charset="utf-8">
<title>bluepinelodge.net business card</title>
<link href="https://fonts.googleapis.com/css2?family=Montserrat:wght@400;500;600&display=swap" rel="stylesheet">
<style>
  :root {
    --stage: #1e1f21;
    --card-light: #ffffff;
    --brand-blue: #2a2f9e;
    --brand-blue-deep: #1d2280;
    --steel: #9aa1ab;
    --rule: #e3e5ea;
    --ink: #3a3d44;
  }
  * { margin: 0; padding: 0; box-sizing: border-box; }
  html, body { width: 1200px; height: 754px; overflow: hidden; }
  body {
    background: var(--stage);
    font-family: "Montserrat", sans-serif;
    position: relative;
  }
  .card {
    position: absolute;
    top: 222px;
    width: 540px;
    height: 309px;
    overflow: hidden;
    border-radius: 2px;
    background: var(--card-light);
    box-shadow: 0 6px 18px rgba(0,0,0,.45);
  }
  .card--back { left: 40px; }
  .card--front { left: 620px; }

  .wordmark {
    display: flex;
    align-items: center;
    gap: 8px;
    font-weight: 600;
    letter-spacing: .2px;
    color: var(--brand-blue);
    white-space: nowrap;
  }
  .wordmark__dot {
    width: 14px; height: 14px; border-radius: 50%;
    background: var(--brand-blue);
    flex: none;
  }
  .card--back .wordmark {
    position: absolute; left: 50%; top: 34px;
    transform: translateX(-50%);
    font-size: 26px;
  }
  .note-area {
    position: absolute; left: 50px; right: 50px; top: 110px;
    list-style: none;
  }
  .note-area li {
    height: 38px;
    border-bottom: 1px solid var(--rule);
  }
  .card--back .back-band {
    position: absolute; left: 0; bottom: 0; width: 100%; height: 10px;
    background: var(--brand-blue);
  }

  .card--front .wordmark {
    position: absolute; left: 28px; top: 128px;
    font-size: 24px;
  }

  .identity { position: absolute; left: 300px; top: 52px; }
  .identity__name {
    font-size: 12px; font-weight: 500; letter-spacing: .6px;
    color: var(--brand-blue); text-transform: uppercase;
  }
  .identity__role { font-size: 7px; color: var(--steel); margin-top: 2px; }

  .contacts { position: absolute; left: 300px; top: 96px; list-style: none; }
  .contacts li {
    display: flex; align-items: center; gap: 7px;
    font-size: 7px; color: var(--ink); height: 13px;
  }
  .contacts svg { width: 8px; height: 8px; fill: var(--ink); flex: none; }

  .swoosh { position: absolute; left: 0; bottom: 0; width: 540px; height: 120px; }
  .address {
    position: absolute; right: 44px; bottom: 16px;
    font-size: 9px; font-weight: 500; color: #ffffff; letter-spacing: .3px;
    white-space: nowrap;
  }
</style>
</head>
<body>
  <section class="card card--back" aria-label="Card back">
    <div class="wordmark"><span class="wordmark__dot"></span>bluepinelodge</div>
    <ul class="note-area" aria-label="Space for a handwritten note">
      <li></li><li></li><li></li><li></li>
    </ul>
    <div class="back-band"></div>
  </section>

  <section class="card card--front" aria-label="Card front">
    <div class="wordmark"><span class="wordmark__dot"></span>bluepinelodge</div>

    <div class="identity">
      <p class="identity__name">Morris Trulsow</p>
      <p class="identity__role">President</p>
    </div>

    <ul class="contacts">
      <li><svg viewBox="0 0 10 10"><path d="M2 0.5l2 2-1 1.2c.6 1.3 1.6 2.3 2.9 2.9l1.2-1 2 2-1.3 1.6C4.5 8.8 1.2 5.5.5 2z"/></svg>555 214 0187</li>
      <li><svg viewBox="0 0 10 10"><rect x="2.5" y="0.5" width="5" height="9" rx="1"/></svg>555 214 0188</li>
      <li><svg viewBox="0 0 10 10"><rect x="0.5" y="3" width="9" height="5" rx="1"/><rect x="2.5" y="0.5" width="5" height="3"/></svg>555 214 0189</li>
      <li><svg viewBox="0 0 10 10"><path d="M0.5 2h9v6h-9z M0.5 2l4.5 3.5L9.5 2"/></svg>morris@bluepinelodge.net</li>
      <li><svg viewBox="0 0 10 10"><circle cx="5" cy="5" r="4.5"/></svg>www.bluepinelodge.net</li>
    </ul>

    <svg class="swoosh" viewBox="0 0 540 120" preserveAspectRatio="none" aria-hidden="true">
      <path d="M0 70 C180 60 380 40 540 6 L540 18 C380 52 180 72 0 80 Z" fill="#c9ccd2"/>
      <path d="M0 84 C180 78 380 60 540 24 L540 120 L0 120 Z" fill="var(--brand-blue)"/>
      <path d="M0 104 C200 100 400 86 540 60 L540 120 L0 120 Z" fill="var(--brand-blue-deep)" opacity=".5"/>
    </svg>
    <p class="address">418 Dunmere Lane Suite 207 Spring TX 77291</p>
  </section>
</body>
</html>
```